Content marketing firm needs a creative out of the box stationary design

Please take a look to the uploaded logo
I need the whole stationary package which include designs for (business card, letterhead, folder, notepad, company profile, small and big envelop, CD and its cover, key medal, header cover for social media pages "facebook, twitter, linkedin, insgram, google+" and website, favicon for website, E-mail signature, flyer, brochure)
Business

```html
<!DOCTYPE html>
<html lang="en">
<head>
<meta charset="utf-8">
<title>Bright Ledger — Stationery Set</title>
<link href="https://fonts.googleapis.com/css2?family=Montserrat:wght@400;600;700&display=swap" rel="stylesheet">
<style>
  :root {
    --brand-blue: #39a3db;
    --brand-dark: #3b3f46;
    --paper: #fbfbfb;
    --ink-soft: #8a8f96;
    --band-top: #2d3035;
    --band-mid: #dcdcdc;
    --band-low: #5b6171;
  }
  * { box-sizing: border-box; margin: 0; padding: 0; }
  html, body { width: 698px; height: 1200px; overflow: hidden; }
  body { font-family: "Montserrat", sans-serif; color: var(--brand-dark); position: relative; background: var(--band-mid); }

  .band { position: absolute; left: 0; width: 698px; }
  .band--top { top: 0; height: 330px; background: var(--band-top); }
  .band--mid { top: 330px; height: 550px; background: var(--band-mid); }
  .band--low { top: 880px; height: 320px; background: var(--band-low); }

  .piece { position: absolute; background: var(--paper); box-shadow: 0 2px 6px rgba(0,0,0,.25); }

  .wordmark { display: flex; align-items: center; gap: 4px; font-weight: 700; color: var(--brand-dark); letter-spacing: .04em; line-height: 1; white-space: nowrap; }
  .wordmark__square { background: var(--brand-blue); flex: none; }
  .wordmark--light { color: #fff; }
  .wordmark--light .wordmark__square { background: #fff; }

  .fine { font-size: 5px; line-height: 1.6; color: var(--ink-soft); }
  .letter-body { font-size: 5.5px; line-height: 1.7; color: #555; }
  .rule { height: 3px; background: var(--brand-blue); position: absolute; left: 0; right: 0; }

  /* Top band */
  .letterhead--small { left: 250px; top: 30px; width: 190px; height: 265px; padding: 18px 16px; }
  .letterhead--small .wordmark { font-size: 8px; }
  .letterhead--small .wordmark__square { width: 8px; height: 8px; }
  .envelope { left: 22px; top: 190px; width: 215px; height: 110px; padding: 14px; }
  .envelope .wordmark { font-size: 8px; }
  .envelope .wordmark__square { width: 8px; height: 8px; }
  .card-blue--small { left: 465px; top: 40px; width: 100px; height: 58px; background: var(--brand-blue); display: flex; align-items: center; justify-content: center; }
  .card-blue--small .wordmark { font-size: 7px; }
  .card-blue--small .wordmark__square { width: 7px; height: 7px; }
  .card-white--small { left: 575px; top: 40px; width: 100px; height: 58px; padding: 8px; }
  .card-white--small .wordmark { font-size: 6px; }
  .card-white--small .wordmark__square { width: 6px; height: 6px; }
  .notepad { left: 500px; top: 130px; width: 120px; height: 170px; padding: 14px 12px; }
  .notepad__rings { position: absolute; top: -4px; left: 10px; right: 10px; height: 6px; background: repeating-linear-gradient(90deg, #777 0 2px, transparent 2px 6px); }
  .notepad .wordmark { font-size: 7px; }
  .notepad .wordmark__square { width: 7px; height: 7px; }
  .notepad__lines { margin-top: 14px; height: 110px; background: repeating-linear-gradient(180deg, transparent 0 11px, #e3e3e3 11px 12px); }

  /* Middle band */
  .letterhead--large { left: 60px; top: 380px; width: 255px; height: 350px; padding: 26px 22px; }
  .letterhead--large .wordmark { font-size: 11px; }
  .letterhead--large .wordmark__square { width: 11px; height: 11px; }
  .letterhead--large .contact { position: absolute; left: 130px; top: 250px; }
  .card-blue--large { left: 350px; top: 630px; width: 165px; height: 94px; background: var(--brand-blue); display: flex; align-items: center; justify-content: center; }
  .card-blue--large .wordmark { font-size: 11px; }
  .card-blue--large .wordmark__square { width: 11px; height: 11px; }
  .card-white--large { left: 350px; top: 740px; width: 165px; height: 94px; padding: 12px; }
  .card-white--large .wordmark { font-size: 8px; }
  .card-white--large .wordmark__square { width: 8px; height: 8px; }
  .card-white--large .contact { position: absolute; right: 12px; bottom: 10px; text-align: right; }
  .name { font-size: 7px; font-weight: 600; color: var(--brand-dark); }

  /* Low band */
  .cd-sleeve { left: 215px; top: 945px; width: 190px; height: 190px; display: flex; align-items: center; justify-content: center; }
  .cd-sleeve .wordmark { font-size: 11px; }
  .cd-sleeve .wordmark__square { width: 11px; height: 11px; }
  .cd-disc { position: absolute; left: 345px; top: 965px; width: 150px; height: 150px; }
  .cd-sleeve-front { z-index: 2; }
</style>
</head>
<body>
  <div class="band band--top"></div>
  <div class="band band--mid"></div>
  <div class="band band--low"></div>

  <section class="piece envelope">
    <div class="wordmark"><span class="wordmark__square"></span>BRIGHT LEDGER</div>
    <p class="fine" style="margin-top:12px">12 Harbor Lane, Eastport<br>+1 555 0142<br>hello@brightledger.co<br>brightledger.co</p>
    <div class="rule" style="bottom:0"></div>
  </section>

  <section class="piece letterhead--small">
    <div class="wordmark"><span class="wordmark__square"></span>BRIGHT LEDGER</div>
    <div class="letter-body" style="margin-top:22px">
      <p>Dear Client,</p>
      <p style="margin-top:6px">Thank you for choosing our studio for your content plan.</p>
      <p>We will share drafts and a full schedule next week.</p>
      <p style="margin-top:10px">Kind regards,</p>
      <p>Team Lead</p>
    </div>
    <div class="rule" style="bottom:0"></div>
  </section>

  <div class="piece card-blue--small"><div class="wordmark wordmark--light"><span class="wordmark__square"></span>BRIGHT LEDGER</div></div>
  <div class="piece card-white--small">
    <div class="wordmark"><span class="wordmark__square"></span>BRIGHT LEDGER</div>
  </div>

  <section class="piece notepad">
    <div class="notepad__rings"></div>
    <div class="wordmark"><span class="wordmark__square"></span>BRIGHT LEDGER</div>
    <div class="notepad__lines"></div>
  </section>

  <section class="piece letterhead--large">
    <div class="wordmark"><span class="wordmark__square"></span>BRIGHT LEDGER</div>
    <p class="fine contact">+1 555 0142<br>hello@brightledger.co<br>brightledger.co<br>12 Harbor Lane, Eastport</p>
  </section>

  <div class="piece card-blue--large"><div class="wordmark wordmark--light"><span class="wordmark__square"></span>BRIGHT LEDGER</div></div>
  <section class="piece card-white--large">
    <div class="wordmark"><span class="wordmark__square"></span>BRIGHT LEDGER</div>
    <div class="contact">
      <p class="name">Tessa Varnell</p>
      <p class="fine">Creative Director<br>+1 555 0142<br>hello@brightledger.co</p>
    </div>
  </section>

  <svg class="cd-disc" viewBox="0 0 150 150" aria-hidden="true">
    <circle cx="75" cy="75" r="74" fill="#f2f2f2"/>
    <circle cx="75" cy="75" r="22" fill="#d6d8db"/>
    <circle cx="75" cy="75" r="9" fill="var(--band-low)"/>
  </svg>
  <section class="piece cd-sleeve cd-sleeve-front">
    <div class="wordmark"><span class="wordmark__square"></span>BRIGHT LEDGER</div>
  </section>
</body>
</html>
```